Business Card Design Project

We need a business card design for a consultancy called 'Amber Ridge'. The design should communicate innovation and professionalism. The colors used should complement our logo. Please include source files for winning design.
Updates

Industry/Entity Type

Business

Colors

Designer to choose colors to be used in the design.

Requirements
Must have
• Card size should be 85mm x 50mm. The back side of the card should be the logo on a black background. The front side should display the name 'Amber Ridge' along with standard information. The front's design should graphically complement the back.
Nice to have
• Any graphical elements in the front the complement the back side (with the logo on a black background) would be a plus.

```html
<!DOCTYPE html>
<html lang="en">
<head>
<meta charset="utf-8">
<title>Amber Ridge – Business Card</title>
<link href="https://fonts.googleapis.com/css2?family=Open+Sans:wght@600;700&display=swap" rel="stylesheet">
<style>
  :root {
    --stage: #3a3d40;
    --card-black: #050505;
    --amber-bright: #ffa534;
    --amber: #f07a1c;
    --amber-deep: #c85a10;
    --ink: #0c0a08;
    --rule: #f6b55a;
    --icon: #ffffff;
  }
  * { margin: 0; padding: 0; box-sizing: border-box; }
  html, body { width: 1200px; height: 857px; overflow: hidden; }
  body {
    background: var(--stage);
    font-family: "Open Sans", Arial, sans-serif;
    position: relative;
  }
  .card {
    position: absolute;
    top: 281px;
    width: 510px;
    height: 300px;
    border-radius: 4px;
    overflow: hidden;
    box-shadow: 0 14px 36px rgba(0,0,0,.45);
  }
  .card--back { left: 60px; background: var(--card-black); }
  .card--front { left: 630px; background: var(--card-black); }

  /* Back: logo on black */
  .logo-lockup {
    position: absolute;
    inset: 0;
    display: flex;
    flex-direction: column;
    align-items: center;
    justify-content: center;
    gap: 22px;
  }
  .logo-lockup__disc {
    width: 118px; height: 118px;
    border-radius: 50%;
    background: var(--amber);
  }
  .logo-lockup__name {
    font-weight: 600;
    font-size: 34px;
    letter-spacing: 2px;
    color: var(--amber-bright);
  }

  /* Front */
  .front__head {
    position: absolute;
    left: 0; top: 0; right: 0; height: 150px;
    background: radial-gradient(ellipse 62% 95% at 52% 62%, var(--amber-bright) 0%, var(--amber) 35%, #7a3a0c 72%, #1a0d05 100%);
  }
  .front__name {
    position: absolute;
    left: 0; right: 0; top: 48px;
    text-align: center;
    font-weight: 700;
    font-size: 50px;
    color: var(--ink);
  }
  .front__body {
    position: absolute;
    left: 0; top: 150px; right: 0; bottom: 0;
    background: linear-gradient(to bottom, #0a0705 0%, #2a1408 25%, var(--amber-deep) 70%, var(--amber) 100%);
  }
  .contact {
    position: absolute;
    left: 22px; right: 40px; top: 36px;
    list-style: none;
  }
  .contact__row {
    display: flex;
    align-items: center;
    gap: 14px;
    height: 26px;
  }
  .contact__icon { width: 16px; height: 16px; flex: none; }
  .contact__rule { flex: 1; height: 2px; background: var(--rule); }
</style>
</head>
<body>
  <section class="card card--back" aria-label="Card back">
    <div class="logo-lockup">
      <div class="logo-lockup__disc"></div>
      <div class="logo-lockup__name">Amber Ridge</div>
    </div>
  </section>

  <section class="card card--front" aria-label="Card front">
    <div class="front__head">
      <h1 class="front__name">Amber Ridge</h1>
    </div>
    <div class="front__body">
      <ul class="contact">
        <li class="contact__row">
          <svg class="contact__icon" viewBox="0 0 16 16" aria-label="Address"><path d="M2 8 L8 2 L14 8 M4 7 V14 H12 V7" fill="none" stroke="var(--icon)" stroke-width="1.6"/></svg>
          <span class="contact__rule"></span>
        </li>
        <li class="contact__row">
          <svg class="contact__icon" viewBox="0 0 16 16" aria-label="Phone"><path d="M4 2 L6.5 5 L5 6.5 Q6.5 9.5 9.5 11 L11 9.5 L14 12 L12 14 Q4 12 2 4 Z" fill="var(--icon)"/></svg>
          <span class="contact__rule"></span>
        </li>
        <li class="contact__row">
          <svg class="contact__icon" viewBox="0 0 16 16" aria-label="Email"><circle cx="8" cy="8" r="2.6" fill="none" stroke="var(--icon)" stroke-width="1.6"/><path d="M10.6 6 V9.5 Q10.6 11 12 11 Q14 11 14 8 A6 6 0 1 0 11 13.2" fill="none" stroke="var(--icon)" stroke-width="1.6"/></svg>
          <span class="contact__rule"></span>
        </li>
        <li class="contact__row">
          <svg class="contact__icon" viewBox="0 0 16 16" aria-label="Website"><rect x="1.5" y="2.5" width="13" height="9" fill="none" stroke="var(--icon)" stroke-width="1.4"/><path d="M5 14 H11" stroke="var(--icon)" stroke-width="1.4"/></svg>
          <span class="contact__rule"></span>
        </li>
      </ul>
    </div>
  </section>
</body>
</html>
```